Flyer for the Harvest of lanterns conference

Flyer design for an annual international conference called "MERIVAL 2017". This is a conference for young adults, so we hope to produce a design that is both professional and appealing to young people in general

We'd like the flyer to showcase the conference brand logo, and clearly highlight the key information to people who will read it.

Target Market(s)

Young people, young adults

Industry/Entity Type

Religious

Font styles to use
Sans Serif

Colors

Designer to choose colors to be used in the design.

Requirements
Must have
• - Should be only one page (Vertical or Horizontal).
• - the MERVAL logo and all the information found in the attached text file. This includes: Main topic: Your sons and daughters shall prophesy,
• Dates and time, location, contact information and everything that is in the attached text file.
Nice to have
• It would be nice to see samples where the white logo is used and another where the black one is used.
Should not have
• This is NOT a folded flyer, we will be sticking it on doors and public places. And we will be printing large simple to put on walls. So only one page with few words like an add (the words are in the attached file)

```html
<!DOCTYPE html>
<html lang="en">
<head>
<meta charset="utf-8">
<title>MERIVAL 2017 – Harvest of Lanterns Conference</title>
<link href="https://fonts.googleapis.com/css2?family=Montserrat:wght@300;700;800&family=Oswald:wght@500;600&family=Norican&family=Quicksand:wght@500&display=swap" rel="stylesheet">
<style>
  :root{
    --sun-core:#fff6c8;
    --sun-orange:#f47a1c;
    --sky-red:#c7261a;
    --deep-red:#7a0f0a;
    --night:#1a0503;
    --banner:#f7cd5c;
    --banner-shade:#d9a93a;
    --ink:#111;
    --venue-ink:#2b2b2b;
    --venue-accent:#7b1410;
    --paper:#f6f3f0;
    --speaker-band-top:#4a4a4a;
    --speaker-band-bottom:#f2f2f2;
    --white:#fff;
    --web-red:#8e1a14;
  }
  *{margin:0;padding:0;box-sizing:border-box}
  html,body{width:927px;height:1200px;overflow:hidden;background:var(--white)}
  .flyer{position:relative;width:927px;height:1200px;overflow:hidden;background:var(--white)}

  .hero-photo{
    position:absolute;left:0;top:0;width:927px;height:675px;
    background:
      radial-gradient(ellipse 170px 150px at 470px 300px,var(--sun-core) 0%,#ffd36a 35%,rgba(244,122,28,0) 100%),
      radial-gradient(ellipse 520px 360px at 470px 260px,var(--sun-orange) 0%,var(--sky-red) 60%,var(--deep-red) 100%);
  }
  .hero-photo::after{
    content:"";position:absolute;left:0;top:390px;width:100%;height:285px;
    background:linear-gradient(90deg,var(--night) 0%,var(--deep-red) 35%,var(--sky-red) 100%);
  }

  .event-title{position:absolute;left:68px;top:28px;font-family:"Montserrat",sans-serif;color:var(--ink);line-height:1}
  .event-title .edition{display:block;color:var(--white);font-weight:800;font-size:47px;letter-spacing:1px}
  .event-title .theme{display:block;font-weight:800;font-size:33px;letter-spacing:3px;margin-top:10px;line-height:1.18}
  .event-title .kind{display:block;font-weight:300;font-size:27px;letter-spacing:1px;margin-top:3px}

  .brand-block{
    position:absolute;left:625px;top:15px;width:235px;height:197px;background:#000;
    display:flex;align-items:center;justify-content:center;
  }
  .brand-block .name{font-family:"Montserrat",sans-serif;font-weight:700;font-size:30px;color:var(--white);letter-spacing:1px}

  .theme-banner{position:absolute;left:0;top:395px;width:927px;height:195px}
  .theme-banner svg{position:absolute;inset:0}
  .theme-banner h2{
    position:absolute;left:110px;top:28px;width:810px;text-align:center;
    font-family:"Norican",cursive;font-weight:400;color:var(--ink);font-size:76px;line-height:.78;
    -webkit-text-stroke:1.6px var(--ink);letter-spacing:1px;
  }

  .dates{
    position:absolute;left:0;top:605px;width:927px;text-align:center;
    font-family:"Oswald",sans-serif;font-weight:500;font-size:44px;color:var(--white);letter-spacing:2px;
  }

  .faces-photo{
    position:absolute;left:0;top:675px;width:927px;height:240px;
    background:radial-gradient(ellipse 420px 160px at 460px 120px,#fbfaf8 0%,var(--paper) 60%,#e6e1dc 100%);
  }

  .venue{position:absolute;left:0;top:684px;width:870px;text-align:center;font-family:"Oswald",sans-serif;color:var(--venue-ink);font-style:normal}
  .venue .hall{font-weight:600;font-size:31px;letter-spacing:2px;display:block;line-height:1.4;margin-bottom:8px}
  .venue .line{display:block;font-weight:500;font-size:25px;letter-spacing:.5px;line-height:43px}
  .venue .hotel{color:var(--venue-accent)}

  .speakers{
    position:absolute;left:0;top:905px;width:927px;height:178px;
    background:linear-gradient(180deg,var(--speaker-band-top) 0%,#9a9a9a 40%,var(--speaker-band-bottom) 100%);
    font-family:"Oswald",sans-serif;font-weight:500;color:var(--ink);text-align:center;letter-spacing:1px;
  }
  .speakers h3{font-weight:500;font-size:21px;margin-top:18px}
  .speakers ul{list-style:none;font-size:23px;line-height:39px;margin-top:0}
  .speakers li{display:inline}
  .speakers li::before{content:"\25CF";font-size:17px;margin:0 8px 0 6px;vertical-align:3px}

  .contact{
    position:absolute;left:0;top:1098px;width:927px;display:flex;justify-content:center;gap:24px;
    font-family:"Quicksand",sans-serif;font-size:22px;color:var(--ink);
  }
  .contact span{display:flex;align-items:center;gap:8px}
  .website{
    position:absolute;left:0;top:1136px;width:927px;text-align:center;
    font-family:"Oswald",sans-serif;font-weight:600;font-size:32px;letter-spacing:7px;color:var(--web-red);
  }
</style>
</head>
<body>
<main class="flyer">
  <div class="hero-photo" role="img" aria-label="Sunset sky with a person jumping joyfully in silhouette against the sun"></div>

  <header class="event-title">
    <span class="edition">MERIVAL 2017</span>
    <span class="theme">HARVEST OF<br>LANTERNS</span>
    <span class="kind">CONFERENCE</span>
  </header>

  <div class="brand-block">
    <span class="name">MERVAL</span>
  </div>

  <section class="theme-banner">
    <svg width="927" height="195" viewBox="0 0 927 195" aria-hidden="true">
      <polygon points="60,10 927,10 927,195 130,195" fill="var(--banner-shade)" opacity=".55"/>
      <polygon points="72,2 927,2 927,188 148,188" fill="var(--banner)"/>
    </svg>
    <h2>Your Sons and Daughters<br>Shall Prophesy</h2>
  </section>

  <p class="dates">1 - 2 - 3 SEPTEMBER 2017 | 6:00PM</p>

  <div class="faces-photo" role="img" aria-label="Faint portraits of young people faded into a light background"></div>

  <address class="venue">
    <span class="hall">CEDAR HALL BALLROOM</span>
    <span class="line hotel">LAKEVIEW GRAND INN</span>
    <span class="line">412 HARBOR ROAD</span>
    <span class="line">EASTBROOK, ME 04999 USA</span>
  </address>

  <section class="speakers">
    <h3>SPEAKERS INCLUDE:</h3>
    <ul>
      <li>PROPHET MARCEL ONDEKO</li><li>BISHOP SAMUEL RUVENDA</li><br>
      <li>PROPHET JOEL AMANI TESORO</li><br>
      <li>PROPHET LUC BEMARI</li><li>PROPHET AARON VELUNDA</li>
    </ul>
  </section>

  <div class="contact">
    <span>
      <svg width="20" height="20" viewBox="0 0 24 24" aria-hidden="true"><circle cx="12" cy="12" r="10.5" fill="none" stroke="currentColor" stroke-width="1.5"/><path d="M8.5 7c.6-.5 1.3-.4 1.6.2l.9 1.8c.2.5 0 1-.4 1.3l-.6.4c.5 1.3 1.6 2.4 2.9 2.9l.4-.6c.3-.4.8-.6 1.3-.4l1.8.9c.6.3.7 1 .2 1.6-1 1.1-2.6 1.2-4 .4C10.2 14.5 9 13.1 8.1 11c-.6-1.5-.6-3 .4-4z" fill="currentColor"/></svg>
      +1 (555) 014 2277
    </span>
    <span>
      <svg width="22" height="18" viewBox="0 0 24 18" aria-hidden="true"><rect x="1" y="1" width="22" height="16" rx="1" fill="none" stroke="currentColor" stroke-width="1.6"/><path d="M1 2l11 8 11-8" fill="none" stroke="currentColor" stroke-width="1.6"/></svg>
      contact@lanterngrove.org
    </span>
  </div>

  <p class="website">WWW.LANTERNHALL.ORG</p>
</main>
</body>
</html>
```